Educational Flashcard Packaging Box Design

We are an educational resource provider in Australia. We have a new product launching for high school students, age 13-18. Thye are flashcards that help students with literacy. We need the box design that will store the cards when the students keep them in the bag at school. They need to be fun and colourful.
Our brand colours are
#06D8D8
#EF0081
#FFC904
#FF9900

The 36 flashcards all have a different colour to make up a rainbow. See the image of the flashcards attached.

The box template is uploaded in the files.
The box dimensions are 91 x 35 x 129mm.
Updates

I had a baby on the 2nd June and am in the hospital until the 8th June so I haven't been able to manage the project.

Target Market(s)

School students age 12 -18

Requirements
Must have
• Name of the product: Brightmark Mastery Flashcards
Fun and engaging design.
Bright colours.
Our logo - attached.
Text:
Get results you can be proud of.
36 flashcards + instructions
Increase key word knowledge and understanding.
(C) Harbourline Study Guild 2021
Newcastle, NSW, Australia.
hsguild.edu.au
Nice to have
• Instructions for the back of the box:
1. Box the key word in every question and check its meaning in the flashcards.
2. Write the meaning above the key word.
3. Use the key word metalanguage in your answer, e.g. describe; use the words characteristics and features in your answer. E.g. explain; use the words cause and effect in your answer and use linking words to demonstrate the relationships.
4. Be sure to add relevant example/s where possible

```html
<!DOCTYPE html>
<html lang="en">
<head>
<meta charset="utf-8">
<title>Brightmark Mastery Flashcards – Box Dieline</title>
<link rel="stylesheet" href="https://fonts.googleapis.com/css2?family=Fredoka:wght@500;600;700&family=Kalam:wght@700&family=Oswald:wght@500&family=Source+Sans+3:wght@700;800&family=Tinos&display=swap">
<style>
  :root{
    --teal:#4cc2c8;
    --deep:#05383a;
    --yellow:#f2e922;
    --banner:#f3ec2c;
    --orange:#f07f23;
    --lilac:#cdb8da;
    --soft-yellow:#fde36e;
    --white:#ffffff;
    --ink:#111111;
    --cut:#2b2b2b;
  }
  *{box-sizing:border-box;margin:0;padding:0}
  html,body{width:1200px;height:1200px;overflow:hidden;background:var(--white)}
  .canvas{position:relative;width:1200px;height:1200px;overflow:hidden}

  .sheet{position:absolute;left:55px;top:231px;width:1098px;height:745px;background:var(--teal)}
  .sheet-yellow{position:absolute;left:0;top:498px;width:100%;height:247px;background:var(--yellow)}

  .dieline{position:absolute;left:0;top:0;width:1200px;height:1200px;pointer-events:none}
  .dieline *{fill:none;stroke:var(--cut);stroke-width:1.2}

  .side{position:absolute;top:244px;width:141px;height:517px}
  .side-title{position:absolute;left:50%;top:50%;width:220px;height:80px;white-space:nowrap;
    transform:translate(-50%,-50%) rotate(-90deg)}
  .side-title .big{position:absolute;left:50%;top:-2px;transform:translateX(-50%);
    font-family:"Source Sans 3",sans-serif;font-weight:800;font-size:44px;color:var(--yellow);letter-spacing:1px}
  .side-title .small{position:absolute;left:50%;top:48px;transform:translateX(-50%);
    font-family:"Oswald",sans-serif;font-weight:500;font-size:20px;color:var(--white);letter-spacing:1px}

  .front{position:absolute;top:244px;width:366px;height:517px;overflow:hidden}
  .brand{position:absolute;left:18px;top:30px;width:100px;display:flex;align-items:center;gap:5px}
  .brand-mark{width:14px;height:14px;background:var(--deep);flex:none}
  .brand-name{font-family:"Source Sans 3",sans-serif;font-weight:800;font-size:11px;line-height:1.05;color:var(--deep);text-transform:uppercase}

  .banner{position:absolute;left:135px;top:28px;width:231px;height:50px}
  .banner svg{position:absolute;inset:0}
  .banner-text{position:absolute;left:38px;top:6px;width:190px;text-align:center;
    font-family:"Kalam",cursive;font-weight:700;font-size:12.5px;line-height:1.45;color:var(--deep);transform:rotate(-2deg)}

  .band{position:absolute;left:0;top:104px;width:100%;height:150px;background:var(--deep)}
  .title{position:absolute;left:0;right:0;top:14px;text-align:center;
    font-family:"Source Sans 3",sans-serif;font-weight:800;font-size:56px;line-height:1;color:var(--white);letter-spacing:0.5px}
  .subtitle{position:absolute;left:0;right:0;top:86px;text-align:center;
    font-family:"Oswald",sans-serif;font-weight:500;font-size:28px;line-height:1;color:var(--white);letter-spacing:1.5px}

  .badge{position:absolute;left:-8px;border:3px solid var(--white);border-radius:0 10px 10px 0;
    font-family:"Fredoka",sans-serif;font-weight:500;color:var(--deep);text-align:center}
  .badge-fun{top:262px;width:149px;height:49px;background:var(--orange);font-size:16px;line-height:15px;padding-top:7px}
  .badge-bright{top:319px;width:149px;height:32px;background:var(--banner);font-size:16px;line-height:26px}

  .cards-art{position:absolute;left:150px;top:270px;width:208px;height:247px;
    background:linear-gradient(160deg,var(--soft-yellow) 0%,var(--lilac) 45%,var(--orange) 100%)}

  .count{position:absolute;left:24px;top:410px;width:72px;text-align:center;
    font-family:"Fredoka",sans-serif;font-weight:700;font-size:58px;line-height:1;color:var(--orange);
    -webkit-text-stroke:3px var(--white);paint-order:stroke fill}
  .count-pill{position:absolute;left:18px;top:467px;width:87px;height:38px;background:var(--deep);border:3px solid var(--white);border-radius:6px;
    font-family:"Fredoka",sans-serif;font-weight:500;font-size:12px;line-height:13px;color:var(--white);text-align:center;padding-top:3px}

  .base-title{position:absolute;left:713px;top:795px;width:367px;text-align:center}
  .base-title .big{font-family:"Source Sans 3",sans-serif;font-weight:800;font-size:40px;line-height:1;color:var(--deep)}
  .base-title .small{margin-top:6px;font-family:"Oswald",sans-serif;font-weight:500;font-size:20px;color:var(--teal);letter-spacing:1px}

  .size-note{position:absolute;left:206px;top:862px;width:370px;text-align:center;
    font-family:"Tinos",serif;font-size:40px;color:var(--ink)}
</style>
</head>
<body>
<main class="canvas">
  <div class="sheet"><div class="sheet-yellow"></div></div>

  <section class="side" style="left:67px">
    <div class="side-title"><span class="big">BRIGHTMARK</span><span class="small">MASTERY FLASHCARDS</span></div>
  </section>

  <section class="front" style="left:206px">
    <div class="brand"><span class="brand-mark"></span><span class="brand-name">Harbourline Study Guild</span></div>
    <div class="banner">
      <svg viewBox="0 0 231 50" preserveAspectRatio="none"><path d="M0,0 L231,6 L231,50 L40,44 L22,20 Z" fill="var(--banner)"/></svg>
      <p class="banner-text">Increase key word knowledge<br>and understanding</p>
    </div>
    <div class="band">
      <h1 class="title">BRIGHTMARK</h1>
      <p class="subtitle">MASTERY FLASHCARDS</p>
    </div>
    <div class="cards-art" role="img" aria-label="Illustration of sample flashcards: Clarify, Interpret and Analyse"></div>
    <div class="badge badge-fun">fun &amp; engaging<br>design</div>
    <div class="badge badge-bright">bright colours</div>
    <div class="count">36</div>
    <div class="count-pill">flashcards +<br>instructions</div>
  </section>

  <section class="side" style="left:572px">
    <div class="side-title"><span class="big">BRIGHTMARK</span><span class="small">MASTERY FLASHCARDS</span></div>
  </section>

  <section class="front" style="left:713px">
    <div class="brand"><span class="brand-mark"></span><span class="brand-name">Harbourline Study Guild</span></div>
    <div class="banner">
      <svg viewBox="0 0 231 50" preserveAspectRatio="none"><path d="M0,0 L231,6 L231,50 L40,44 L22,20 Z" fill="var(--banner)"/></svg>
      <p class="banner-text">Increase key word knowledge<br>and understanding</p>
    </div>
    <div class="band">
      <h2 class="title">BRIGHTMARK</h2>
      <p class="subtitle">MASTERY FLASHCARDS</p>
    </div>
    <div class="cards-art" role="img" aria-label="Illustration of sample flashcards: Clarify, Interpret and Analyse"></div>
    <div class="badge badge-fun">fun &amp; engaging<br>design</div>
    <div class="badge badge-bright">bright colours</div>
    <div class="count">36</div>
    <div class="count-pill">flashcards +<br>instructions</div>
  </section>

  <div class="base-title"><div class="big">BRIGHTMARK</div><div class="small">MASTERY FLASHCARDS</div></div>
  <p class="size-note">91x35x129mm</p>

  <svg class="dieline" viewBox="0 0 1200 1200">
    <rect x="67" y="244" width="1013" height="517"/>
    <line x1="206" y1="244" x2="206" y2="761"/>
    <line x1="572" y1="244" x2="572" y2="761"/>
    <line x1="713" y1="244" x2="713" y2="761"/>
    <path d="M1080,244 L1141,252 L1141,744 L1080,761"/>
    <line x1="1091" y1="330" x2="1125" y2="304"/>
    <line x1="1091" y1="456" x2="1125" y2="430"/>
    <line x1="1091" y1="590" x2="1125" y2="564"/>
    <line x1="1091" y1="723" x2="1125" y2="697"/>
    <path d="M77,761 L77,861 L158,861 L166,856 L191,786 L204,778 L204,761"/>
    <path d="M574,761 L574,778 L587,786 L612,856 L620,861 L701,861 L701,761"/>
    <rect x="713" y="761" width="367" height="142"/>
    <path d="M716,903 L716,928 Q716,963 751,963 L1042,963 Q1077,963 1077,928 L1077,903"/>
    <path d="M742,903 L742,900 L1050,900 L1050,903"/>
  </svg>
</main>
</body>
</html>
```